Flyer Design Project

I need a flyer design to pass out to promote my business and to bring in more business. My business is a auto body shop and we do auto body repair on all makes and models. We take all types of insurance work and cash deals are welcome. We type of paint we use is KTV so i would like the KTV logo somewhere on the flyer.I would also like to include that we offer free estimates.
Updates

I forgot to include the following information to my shop

Address : 3847 N. Willowmere St
                 San Mateo, Ca 94402

Tel : 650-318-4962

Website : www.TrueLineCollision.example

please include that cash deals are welcome, we offer 24 hours drop off service, and we offer mobile estimate service

Industry/Entity Type

Insurance

Requirements
Must have
• Must have my company logo in it. Must be eye catching.

```html
<!DOCTYPE html>
<html lang="en">
<head>
<meta charset="utf-8">
<title>TrueLine Collision – Flyer</title>
<link rel="stylesheet" href="https://fonts.googleapis.com/css2?family=Kanit:ital,wght@0,700;1,800;1,900&family=Open+Sans:ital,wght@1,600;1,700&display=swap">
<style>
  :root {
    --red: #d4111c;
    --red-deep: #7a0309;
    --red-bright: #f0232b;
    --black: #0b0b0b;
    --white: #ffffff;
    --silver: #c9c9c9;
    --footer-grey: #6b6b6b;
    --rule: #bdbdbd;
  }
  * { margin: 0; padding: 0; box-sizing: border-box; }
  html, body { width: 858px; height: 1200px; overflow: hidden; background: var(--black); }
  .flyer {
    position: relative;
    width: 858px;
    height: 1200px;
    overflow: hidden;
    background:
      radial-gradient(ellipse 700px 420px at 640px 170px, #b00d16 0%, transparent 70%),
      linear-gradient(180deg, #4a0206 0%, #9c0b12 22%, #5a0307 42%, #1a0a0a 58%, var(--black) 70%);
    font-family: "Open Sans", Arial, sans-serif;
    color: var(--white);
  }
  .swooshes { position: absolute; inset: 0; }

  .brand {
    position: absolute; left: 48px; top: 42px;
    display: flex; align-items: center; gap: 14px;
  }
  .brand-dot {
    width: 70px; height: 70px; border-radius: 50%;
    background: var(--red);
  }
  .brand-name {
    font-family: "Kanit", Arial, sans-serif;
    font-weight: 700;
    font-size: 40px; line-height: 1.05;
    color: var(--white);
  }

  .call {
    position: absolute; right: 46px; top: 30px;
    text-align: right;
    font-style: italic; font-weight: 700;
  }
  .call-label { font-size: 29px; line-height: 1.1; margin-right: 44px; }
  .call-number { font-size: 36px; line-height: 1.15; letter-spacing: 1px; }

  .headline {
    position: absolute; left: 82px; top: 268px;
    font-family: "Kanit", Arial, sans-serif;
    font-style: italic; font-weight: 900;
    font-size: 56px; line-height: 62px;
    text-shadow: 0 4px 6px rgba(0,0,0,.45);
  }
  .headline span { display: block; }
  .headline span + span { padding-left: 95px; }

  .car-art {
    position: absolute; left: 215px; top: 410px;
    width: 643px; height: 320px;
    border-radius: 48% 40% 18% 22% / 40% 45% 30% 35%;
    background: radial-gradient(ellipse at 45% 45%, #ff3a3f 0%, #d3101a 45%, #7d0710 80%, rgba(20,0,0,0) 100%);
  }

  .services {
    position: absolute; left: 48px; top: 742px;
    list-style: none;
    font-style: italic; font-weight: 600;
    font-size: 26px;
  }
  .services li {
    display: flex; align-items: center; gap: 16px;
    height: 44px;
    border-bottom: 1.5px solid var(--rule);
    width: var(--w);
    margin-left: var(--x);
  }
  .services li:last-child { border-bottom: none; }
  .tick { width: 24px; height: 24px; flex: none; }

  .feature {
    position: absolute; top: 770px; width: 170px;
    text-align: center;
  }
  .feature-ring {
    width: 126px; height: 126px; margin: 0 auto;
    border: 9px solid var(--red); border-radius: 50%;
    background: var(--black);
    display: flex; align-items: center; justify-content: center;
  }
  .feature-ring .big {
    font-family: "Kanit", Arial, sans-serif; font-weight: 700;
    font-size: 50px; letter-spacing: -1px;
  }
  .feature-label {
    margin-top: 10px;
    font-family: "Kanit", Arial, sans-serif; font-weight: 700;
    font-size: 25px; line-height: 28px; letter-spacing: 1px;
  }
  .feature.dropoff { left: 444px; }
  .feature.mobile { left: 660px; }

  .cash {
    position: absolute; left: 0; right: 0; top: 1030px;
    text-align: center;
    font-family: "Kanit", Arial, sans-serif;
    font-style: italic; font-weight: 900;
    font-size: 46px; letter-spacing: 1px;
    color: var(--red-bright);
  }

  .footer {
    position: absolute; left: 0; bottom: 0;
    width: 858px; height: 96px;
    background: var(--footer-grey);
    display: flex; align-items: center; justify-content: space-between;
    padding: 0 36px 0 46px;
    font-style: italic;
  }
  .address { font-weight: 600; font-size: 21px; line-height: 28px; }
  .website { font-weight: 700; font-size: 30px; }
</style>
</head>
<body>
<main class="flyer">
  <svg class="swooshes" width="858" height="1200" viewBox="0 0 858 1200" aria-hidden="true">
    <defs>
      <linearGradient id="silverSweep" x1="0" y1="0" x2="1" y2="0">
        <stop offset="0" stop-color="#e8e8e8"/>
        <stop offset=".6" stop-color="#9a9a9a"/>
        <stop offset="1" stop-color="#9a9a9a" stop-opacity="0"/>
      </linearGradient>
      <linearGradient id="redSweep" x1="0" y1="0" x2="1" y2="0">
        <stop offset="0" stop-color="#ff3b3b" stop-opacity="0"/>
        <stop offset=".5" stop-color="#ff4a4a" stop-opacity=".55"/>
        <stop offset="1" stop-color="#ff3b3b" stop-opacity="0"/>
      </linearGradient>
    </defs>
    <path d="M0 150 C250 60 520 70 858 20 L858 60 C560 110 300 110 0 190 Z" fill="url(#redSweep)"/>
    <path d="M0 390 C300 300 600 280 858 320 L858 350 C600 320 300 340 0 430 Z" fill="url(#redSweep)"/>
    <path d="M0 450 C180 430 300 440 420 470 C300 480 160 520 0 600 Z" fill="url(#silverSweep)"/>
    <path d="M0 620 C200 600 380 620 560 700 C380 660 200 660 0 690 Z" fill="#3a3a3a" opacity=".7"/>
  </svg>

  <div class="brand">
    <span class="brand-dot"></span>
    <span class="brand-name">TrueLine<br>Collision</span>
  </div>

  <div class="call">
    <div class="call-label">Call Us Now</div>
    <div class="call-number">650-318-4962</div>
  </div>

  <h1 class="headline"><span>Proudly Serving</span><span>Entire Bay Area</span></h1>

  <div class="car-art" role="img" aria-label="Illustration of a red sports car"></div>

  <ul class="services">
    <li style="--x:48px;--w:306px"><svg class="tick" viewBox="0 0 24 24"><circle cx="12" cy="12" r="12" fill="var(--red)"/><path d="M6 12.5l4 4 8-9" stroke="#fff" stroke-width="3" fill="none"/></svg>FRAMEWORKS</li>
    <li style="--x:36px;--w:318px"><svg class="tick" viewBox="0 0 24 24"><circle cx="12" cy="12" r="12" fill="var(--red)"/><path d="M6 12.5l4 4 8-9" stroke="#fff" stroke-width="3" fill="none"/></svg>COLLISION REPAIR</li>
    <li style="--x:28px;--w:318px"><svg class="tick" viewBox="0 0 24 24"><circle cx="12" cy="12" r="12" fill="var(--red)"/><path d="M6 12.5l4 4 8-9" stroke="#fff" stroke-width="3" fill="none"/></svg>AUTO PAINTING</li>
    <li style="--x:20px;--w:312px"><svg class="tick" viewBox="0 0 24 24"><circle cx="12" cy="12" r="12" fill="var(--red)"/><path d="M6 12.5l4 4 8-9" stroke="#fff" stroke-width="3" fill="none"/></svg>COLOUR MATCHING</li>
    <li style="--x:10px;--w:310px"><svg class="tick" viewBox="0 0 24 24"><circle cx="12" cy="12" r="12" fill="var(--red)"/><path d="M6 12.5l4 4 8-9" stroke="#fff" stroke-width="3" fill="none"/></svg>CAR DETAILING</li>
    <li style="--x:0px;--w:300px"><svg class="tick" viewBox="0 0 24 24"><circle cx="12" cy="12" r="12" fill="var(--red)"/><path d="M6 12.5l4 4 8-9" stroke="#fff" stroke-width="3" fill="none"/></svg>DENT REMOVAL</li>
  </ul>

  <div class="feature dropoff">
    <div class="feature-ring"><span class="big">24/7</span></div>
    <div class="feature-label">hours<br>drop off<br>service</div>
  </div>

  <div class="feature mobile">
    <div class="feature-ring">
      <svg width="44" height="74" viewBox="0 0 44 74" aria-label="Mobile phone" role="img">
        <rect x="8" y="0" width="5" height="14" rx="2" fill="#fff"/>
        <rect x="2" y="10" width="40" height="62" rx="7" fill="#fff"/>
        <rect x="8" y="17" width="28" height="18" rx="2" fill="var(--black)"/>
        <g fill="var(--black)">
          <rect x="9" y="40" width="6" height="5"/><rect x="19" y="40" width="6" height="5"/><rect x="29" y="40" width="6" height="5"/>
          <rect x="9" y="49" width="6" height="5"/><rect x="19" y="49" width="6" height="5"/><rect x="29" y="49" width="6" height="5"/>
          <rect x="9" y="58" width="6" height="5"/><rect x="19" y="58" width="6" height="5"/><rect x="29" y="58" width="6" height="5"/>
        </g>
      </svg>
    </div>
    <div class="feature-label">mobile<br>estimate<br>service</div>
  </div>

  <p class="cash">Cash deals are welcome</p>

  <footer class="footer">
    <address class="address">3847 N. Willowmere St<br>San Mateo, Ca 94402</address>
    <span class="website">www.TrueLineCollision.example</span>
  </footer>
</main>
</body>
</html>
```